STI/STD Medical Clinic- Wellspring Crest Partners, Inc Website

We are a Wellspring Crest in florida looking for a website. We want to be professional but also playful. We want a buildout similar to the website listed below as our clinic is very similar to theirs.

This is a great example of a clinic doing similar stuff as us. We obviously do not want their color scheme but their format and buildout work. Please see our logo attached for color schemes etc.

https://bluefernclinicmiami.org

Industry/Entity Type

Medical

Coding

Coded - Design and coding required

Number of Pages Required

5+ page

Font styles to use
Sans Serif

```html
<!DOCTYPE html>
<html lang="en">
<head>
<meta charset="utf-8">
<title>Wellspring Crest Partners – Services</title>
<link href="https://fonts.googleapis.com/css2?family=Roboto:wght@400;500;700&display=swap" rel="stylesheet">
<style>
:root{
  --blue:#1877e0;
  --blue-dark:#0f5fbf;
  --ink:#222831;
  --text:#4a4f57;
  --muted:#8a8f96;
  --white:#ffffff;
  --field:#f4f4f4;
  --shade:#3b4656;
}
*{margin:0;padding:0;box-sizing:border-box}
html,body{width:1200px;height:4315px;overflow:hidden}
body{position:relative;font-family:'Roboto',sans-serif;color:var(--text);background:var(--white)}
.abs{position:absolute}
.topbar{left:0;top:0;width:1200px;height:64px;background:var(--blue);color:var(--white);font-size:16px;font-weight:500}
.topbar .mail{left:22px;top:21px;display:flex;align-items:center;gap:12px}
.topbar .hours{left:322px;top:21px;display:flex;align-items:center;gap:12px}
.dot-ico{width:22px;height:22px;border-radius:50%;background:var(--white);display:inline-block}
.social{right:20px;top:22px;display:flex;gap:26px}
.social span{width:20px;height:20px;border-radius:50%;background:var(--white)}
.header{left:0;top:64px;width:1200px;height:100px;background:var(--white);border-bottom:1px solid #e4e8ee}
.brand{left:22px;top:34px;display:flex;align-items:center;gap:10px;font-size:26px;font-weight:700;color:var(--blue)}
.brand i{width:26px;height:26px;border-radius:50%;background:var(--blue);display:block}
.nav{left:257px;top:40px;display:flex;gap:56px;font-size:17px;font-weight:500;color:var(--ink)}
.nav .on{color:var(--blue)}
.donate{left:967px;top:24px;width:170px;height:52px;background:var(--blue);color:var(--white);font-size:19px;display:flex;align-items:center;justify-content:center;gap:14px}
.donate i{width:18px;height:16px;background:var(--white);border-radius:3px;display:block}
.hero{left:0;top:164px;width:1200px;height:660px;background:linear-gradient(135deg,#5a6472 0%,#8793a2 40%,#b9c2cc 65%,#6d7886 100%)}
.hero-title{left:27px;top:372px;font-size:44px;font-weight:700;color:var(--white);letter-spacing:1px}
.crumb{left:27px;top:430px;font-size:16px;font-weight:700;color:var(--white);display:flex;align-items:center;gap:26px}
.intro{left:27px;top:555px;width:1146px;height:260px;background:var(--white);text-align:center}
.intro h2{margin-top:22px;font-size:43px;font-weight:500;color:var(--ink);letter-spacing:1px}
.intro .rule{margin:26px auto 0;width:590px;display:flex;align-items:center;justify-content:space-between}
.intro .rule span{width:218px;height:2px;background:#7fb1e8}
.intro p{margin:26px auto 0;width:780px;font-size:18px;line-height:29px}
.appt{left:0;top:824px;width:1200px;height:1000px;background:linear-gradient(180deg,#68768a 0%,#4c5a6d 40%,#3c4652 75%,#4a4e54 100%)}
.appt h3{left:32px;top:990px;font-size:32px;font-weight:700;color:var(--white)}
.field{height:50px;background:var(--field);border:1px solid #ddd;font-size:18px;color:#333;padding:0 14px;display:flex;align-items:center;justify-content:space-between}
.field small{font-size:10px;color:#aaa}
.book{left:265px;top:1468px;width:313px;height:52px;background:var(--blue);color:var(--white);font-size:18px;font-weight:500;letter-spacing:1px;display:flex;align-items:center;justify-content:center}
.appt-note{left:21px;top:1554px;font-size:18px;line-height:30px;color:var(--white)}
.ph{position:absolute}
.best-title{left:0;top:1860px;width:1200px;text-align:center;font-size:42px;font-weight:700;color:var(--blue);letter-spacing:-1px}
.best-lead{left:0;top:1985px;width:1200px;text-align:center;font-size:18px;line-height:29px;color:var(--ink)}
.svc{width:288px;height:307px;padding:14px 10px 0 12px}
.svc h4{font-size:26px;font-weight:500;color:var(--ink);letter-spacing:-1px}
.svc p{margin-top:16px;font-size:18px;line-height:29px;color:var(--text)}
.svc .btn{margin-top:20px;display:inline-block;width:126px;height:38px;line-height:38px;text-align:center;background:var(--blue);color:var(--white);font-size:16px;font-weight:500}
.svc.right{text-align:right;padding:14px 12px 0 10px}
.svc.faded p,.svc.faded h4{color:var(--muted)}
.svc.faded h4{color:var(--ink)}
.case{left:0;top:2777px;width:1200px;height:1060px;background:linear-gradient(180deg,#5b6677 0%,#4b5667 40%,#3f4a5a 80%,#566273 100%)}
.case-title{left:0;top:2855px;width:1200px;text-align:center;font-size:44px;font-weight:700;color:var(--white)}
.case-lead{left:0;top:2937px;width:1200px;text-align:center;font-size:18px;line-height:29px;color:var(--white)}
.card{top:3122px;height:448px;background:var(--white);text-align:center}
.card .img{height:215px}
.card h5{margin-top:38px;font-size:26px;font-weight:500;color:var(--ink);letter-spacing:-1px}
.card p{margin-top:12px;font-size:18px;line-height:23px;color:var(--ink)}
.card .btn{margin:18px auto 0;width:126px;height:42px;line-height:42px;background:var(--blue);color:var(--white);font-size:16px;font-weight:500}
.explore{left:520px;top:3667px;width:162px;height:45px;background:var(--blue);color:var(--white);font-size:17px;font-weight:500;display:flex;align-items:center;justify-content:center}
.foot h6{font-size:17px;font-weight:700;color:var(--ink)}
.foot-about{left:32px;top:4005px;width:300px;font-size:15px;line-height:23px;color:#3a5fa8}
.links{left:370px;top:3897px}
.links li{list-style:none;font-size:15px;color:var(--ink);height:49px;display:flex;align-items:center;gap:10px}
.hours-tbl{left:561px;top:3897px;font-size:15px;color:#555}
.hours-tbl .row{display:flex;align-items:center;height:43px}
.hours-tbl .d{width:113px}
.hours-tbl .ln{width:58px;height:1px;background:#333;margin-right:22px}
.contact{left:972px;top:3897px;font-size:15px;color:var(--ink)}
.contact .it{display:flex;gap:14px;align-items:flex-start;margin-top:20px;line-height:22px}
.copy{left:0;top:4269px;width:1200px;height:46px;background:var(--blue);color:var(--white);font-size:14px;display:flex;align-items:center;justify-content:center}
</style>
</head>
<body>

<div class="abs topbar">
  <div class="abs mail"><span class="dot-ico"></span>hello@wellspringcrest.org</div>
  <div class="abs hours"><span class="dot-ico"></span>Mon - Sat: 8.00 am - 7.00 pm</div>
  <div class="abs social"><span></span><span></span><span></span><span></span></div>
</div>

<div class="abs header">
  <div class="abs brand"><i></i>Wellspring Crest</div>
  <nav class="abs nav"><span>Home</span><span>About</span><span class="on">Services</span><span>News</span></nav>
  <div class="abs donate"><i></i>Donate</div>
</div>

<div class="abs hero" role="img" aria-label="Smiling doctor with medical team in a hospital corridor"></div>
<div class="abs hero-title">Services style one</div>
<div class="abs crumb"><span>Home</span>
  <svg width="22" height="18" viewBox="0 0 22 18"><path d="M2 9h16M11 2l7 7-7 7" stroke="#fff" stroke-width="3" fill="none"/></svg>
  <span>Services</span></div>

<div class="abs appt" role="img" aria-label="City street with palm trees, darkened"></div>

<svg class="abs" style="left:0;top:790px" width="1200" height="110" viewBox="0 0 1200 110">
  <path d="M0 20 C120 80 230 90 360 50 C480 10 560 60 680 45 C800 30 880 0 1000 30 C1090 50 1150 40 1200 30 L1200 0 L0 0Z" fill="#d9dde3"/>
  <path d="M0 10 C90 60 200 75 330 40 C450 5 540 50 660 35 C790 20 870 -5 990 20 C1080 40 1150 30 1200 20 L1200 0 L0 0Z" fill="#ffffff"/>
  <path d="M0 40 C140 100 260 95 380 70 C500 45 600 90 720 70 C840 50 960 40 1060 60 C1130 72 1180 60 1200 55 L1200 45 C1150 55 1080 55 990 40 C880 20 790 50 670 60 C550 70 460 30 360 55 C240 85 110 80 0 30Z" fill="#b9c0ca" opacity=".7"/>
</svg>

<div class="abs intro">
  <h2>Services that we provide</h2>
  <div class="rule"><span></span>
    <svg width="56" height="50" viewBox="0 0 56 50"><path d="M28 48 C10 34 2 26 2 15 C2 7 8 2 15 2 C21 2 25 5 28 10 C31 5 35 2 41 2 C48 2 54 7 54 15 C54 26 46 34 28 48Z" fill="#1877e0"/><path d="M8 22h12l4-7 5 14 4-9h15" stroke="#fff" stroke-width="3" fill="none"/></svg>
  <span></span></div>
  <p>Lorem ipsum dolor sit amet, consectetur adipiscing elit. Ut elit tellus, luctus nec ullamcorper mattis, pulvinar dapibus leo.</p>
</div>

<h3 class="abs" style="left:32px;top:990px;font-size:32px;font-weight:700;color:#fff">Get Your Appointment</h3>
<div class="abs field" style="left:32px;top:1068px;width:546px">Select Departmenet<small>▾</small></div>
<div class="abs field" style="left:32px;top:1146px;width:546px">Select Specialist<small>▾</small></div>
<div class="abs field" style="left:32px;top:1225px;width:546px">Select Doctor<small>▾</small></div>
<div class="abs field" style="left:32px;top:1304px;width:261px">Your Name</div>
<div class="abs field" style="left:317px;top:1304px;width:261px">Your Email</div>
<div class="abs field" style="left:32px;top:1381px;width:546px">Select Date</div>
<div class="abs book">BOOK AN APPOINTMENT</div>
<div class="abs appt-note">Get your appointment through online and remain safe at your home.<br>Because your safety is our first priority</div>

<div class="ph" style="left:612px;top:997px;width:159px;height:243px;background:linear-gradient(135deg,#9fb8cf,#c8d6e2)" role="img" aria-label="Red heart held in front of a doctor's coat"></div>
<div class="ph" style="left:784px;top:997px;width:374px;height:419px;background:linear-gradient(135deg,#4a4038,#9a8c7c 60%,#d8d4cc)" role="img" aria-label="Doctor on a video call with a patient on a laptop"></div>
<div class="ph" style="left:612px;top:1254px;width:345px;height:343px;background:linear-gradient(135deg,#e6e6e6,#b8b0a8 60%,#6a5a4c)" role="img" aria-label="Laptop showing an online doctor consultation"></div>
<div class="ph" style="left:972px;top:1430px;width:186px;height:167px;background:linear-gradient(135deg,#dfe6ec,#a9b7c4)" role="img" aria-label="Doctor writing at a desk by a window"></div>

<div class="abs best-title">Our Best Services</div>
<div class="abs best-lead">Lorem ipsum dolor sit amet, consectetur adipiscing elit. Ut elit tellus, luctus nec<br>ullamcorper mattis, pulvinar dapibus leo.</div>

<div class="ph" style="left:22px;top:2119px;width:290px;height:307px;background:linear-gradient(135deg,#2a5f9a,#6fa2d0 60%,#b9d3ea)" role="img" aria-label="Surgeons in masks during an operation"></div>
<div class="abs svc" style="left:312px;top:2119px"><h4>Add sub tittle</h4><p>Lorem ipsum dolor sit amet, consectetur adipiscing elit. Ut elit tellus, luctus nec ullamcorper mattis, pulvinar dapibus leo.</p><span class="btn">Read more</span></div>
<div class="ph" style="left:602px;top:2119px;width:288px;height:307px;background:linear-gradient(135deg,#3d6a9a,#8fb1d2 60%,#c6d8ea)" role="img" aria-label="Surgeon at an operating microscope"></div>
<div class="abs svc faded" style="left:890px;top:2119px"><h4>Add sub tittle</h4><p>Lorem ipsum dolor sit amet, consectetur adipiscing elit. Ut elit tellus, luctus nec ullamcorper mattis, pulvinar dapibus leo.</p><span class="btn">Read more</span></div>

<div class="abs svc right" style="left:22px;top:2426px;width:290px"><h4>Add sub tittle</h4><p>Lorem ipsum dolor sit amet, consectetur adipiscing elit. Ut elit tellus, luctus nec ullamcorper mattis, pulvinar dapibus leo.</p><span class="btn">Read more</span></div>
<div class="ph" style="left:312px;top:2426px;width:290px;height:307px;background:linear-gradient(135deg,#5d84ad,#9eb9d4 55%,#4a6a8c)" role="img" aria-label="Surgical team operating"></div>
<div class="abs svc right" style="left:602px;top:2426px;width:288px"><h4>Add sub tittle</h4><p>Lorem ipsum dolor sit amet, consectetur adipiscing elit. Ut elit tellus, luctus nec ullamcorper mattis, pulvinar dapibus leo.</p><span class="btn">Read more</span></div>
<div class="ph" style="left:890px;top:2426px;width:288px;height:307px;background:linear-gradient(135deg,#eef0f2,#c9cdd2 60%,#8c8f94)" role="img" aria-label="Child at an eye examination with an optician"></div>

<div class="abs case" role="img" aria-label="Hospital ward with beds, darkened"></div>
<div class="abs case-title">Case Study</div>
<div class="abs case-lead">Lorem ipsum dolor sit amet, consectetur adipiscing elit. Ut elit tellus, luctus nec<br>ullamcorper mattis, pulvinar dapibus leo.</div>

<div class="abs card" style="left:22px;width:368px"><div class="img" role="img" aria-label="Doctor talking with a patient" style="background:linear-gradient(135deg,#cfd6de,#9fb0c2 60%,#e8e2da)"></div><h5>This is the heading</h5><p>Lorem ipsum dolor sit amet<br>consectetur adipiscing elit dolor</p><div class="btn">Click Here</div></div>
<div class="abs card" style="left:412px;width:377px"><div class="img" role="img" aria-label="Child at an eye test" style="background:linear-gradient(135deg,#f1f1f1,#c8ccd1 60%,#8d9096)"></div><h5>This is the heading</h5><p>Lorem ipsum dolor sit amet<br>consectetur adipiscing elit dolor</p><div class="btn">Click Here</div></div>
<div class="abs card" style="left:811px;width:369px"><div class="img" role="img" aria-label="Surgeon at an operating microscope" style="background:linear-gradient(135deg,#3d6a9a,#8fb1d2 60%,#c6d8ea)"></div><h5>This is the heading</h5><p>Lorem ipsum dolor sit amet<br>consectetur adipiscing elit dolor</p><div class="btn">Click Here</div></div>

<div class="abs explore">Explore more</div>

<svg class="abs" style="left:0;top:3750px" width="1200" height="90" viewBox="0 0 1200 90">
  <path d="M0 50 C120 20 240 30 360 45 C480 60 560 20 700 30 C840 40 940 10 1060 25 C1130 34 1170 30 1200 28 L1200 90 L0 90Z" fill="#c9ced6"/>
  <path d="M0 65 C140 40 260 50 380 60 C500 70 600 40 740 48 C880 56 980 35 1090 48 C1150 55 1180 50 1200 48 L1200 90 L0 90Z" fill="#ffffff"/>
</svg>

<div class="foot">
  <div class="abs brand" style="top:3930px;left:40px"><i></i>Wellspring Crest</div>
  <div class="abs foot-about"><p>Lorem ipsum dolor sit amet, consectetur adipiscing elit. Ut elit tellus, luctus nec</p><p style="margin-top:14px">Lorem ipsum dolor sit amet, consectetur adipiscing elit. Ut elit tellus, luctus nec</p></div>

  <div class="abs links"><h6>Important link</h6>
    <ul style="margin-top:8px">
      <li>✓ About us</li><li>✓ Department</li><li>✓ Services</li><li>✓ Study case</li><li>✓ Contact us</li>
    </ul></div>

  <div class="abs hours-tbl"><h6>Open hour</h6>
    <div style="margin-top:10px">
      <div class="row"><span class="d">Monday</span><span class="ln"></span>8:00 am – 9:30 pm</div>
      <div class="row"><span class="d">Tuesday</span><span class="ln"></span>8:00 am – 9:30 pm</div>
      <div class="row"><span class="d">Wednesday</span><span class="ln"></span>8:00 am – 9:30 pm</div>
      <div class="row"><span class="d">Friday</span><span class="ln"></span>8:00 am – 9:30 pm</div>
      <div class="row"><span class="d">Saturday</span><span class="ln"></span>8:00 am – 9:30 pm</div>
      <div class="row"><span class="d">Sunday</span><span class="ln"></span>8:00 am – 9:30 pm</div>
    </div></div>

  <div class="abs contact"><h6>Contact info</h6>
    <div class="it" style="margin-top:26px"><svg width="16" height="22" viewBox="0 0 16 22"><path d="M8 1C4 1 1 4 1 8c0 5 7 13 7 13s7-8 7-13c0-4-3-7-7-7z" fill="#111"/><circle cx="8" cy="8" r="3" fill="#fff"/></svg><span>456 Palmetto Ave Suite<br>210, Florida, USA</span></div>
    <div class="it"><svg width="18" height="18" viewBox="0 0 18 18"><path d="M4 1l3 4-2 2c1 3 3 5 6 6l2-2 4 3-2 3C8 17 1 10 1 3z" fill="#111"/></svg><span>+1-305-555-0142</span></div>
    <div class="it"><span style="width:18px;height:18px;border-radius:50%;background:#111;display:block"></span><span>hello@wellspringcrest.org</span></div>
  </div>
</div>

<div class="abs copy">Copyright ©2022 Wellspring Crest. All Rights Reserved by Bluefern Studio</div>

</body>
</html>
```